Industrial Company needing new business cards

We are a newly branded Industrial trade company. We specialise in Electrical, Mechanical and Air-conditioning.

I would like to see designs single sided. Focusing on the color scheme white/red/black and possibly gray. Possibly make it a black card with white writting... but open to all designs.

I would like the design to be professional, sleek and to the point.

Industry/Entity Type

Business

Contact Information for Business Card

Tom Harwell
Managing Director / Electrician
tomwork@vandilo.com.au
417 Calloway Street, Pembrook NSW 2458
Mobile: 0497551832
www.harwellindustrialgroup.com.au

Requirements
Must have
• Must be able to be sent in a manner that i can change the details for each employee.
• Our logo
Nice to have
• Would like it to somehow have " incorporating Barvo Group Pty Ltd" as this is the company we have taken over.
Should not have
• No yellow!!!
• must not simply place "barvo group" randomly on the business card. refer nice to have.

```html
<!DOCTYPE html>
<html lang="en">
<head>
<meta charset="utf-8">
<title>Harwell Industrial Group – Business Cards</title>
<link href="https://fonts.googleapis.com/css2?family=Open+Sans:wght@400;600;700&display=swap" rel="stylesheet">
<style>
  :root {
    --page: #e6e3df;
    --card-black: #0d0d0d;
    --card-charcoal: #1c1c1c;
    --brand-red: #e8303a;
    --deep-red: #5a0c12;
    --ink-white: #ffffff;
    --ink-grey: #bdbdbd;
    --ink-dark: #2a0a0c;
  }
  * { box-sizing: border-box; margin: 0; padding: 0; }
  html, body { width: 1200px; height: 913px; overflow: hidden; }
  body {
    background: var(--page);
    font-family: "Open Sans", Arial, sans-serif;
    position: relative;
  }
  .card {
    position: absolute;
    width: 540px;
    height: 310px;
    background: var(--card-black);
    overflow: hidden;
    box-shadow: 0 10px 28px rgba(0,0,0,.25);
  }
  .card--front { left: 60px; top: 150px; }
  .card--back  { left: 600px; top: 460px;
    background: linear-gradient(120deg, var(--deep-red) 0%, var(--card-charcoal) 45%, var(--card-black) 100%); }

  .card__band { position: absolute; inset: 0; }

  .brand {
    position: absolute;
    display: flex;
    align-items: center;
    gap: 10px;
  }
  .brand__dot { width: 12px; height: 12px; background: var(--brand-red); border-radius: 50%; }
  .brand__name {
    color: var(--ink-white);
    font-weight: 700;
    text-transform: uppercase;
    letter-spacing: .04em;
  }
  .brand__tagline {
    position: absolute;
    color: var(--ink-white);
    font-size: 8px;
    letter-spacing: .06em;
    text-transform: uppercase;
  }
  .card--front .brand { right: 30px; top: 30px; }
  .card--front .brand__name { font-size: 17px; }
  .card--front .brand__tagline { right: 30px; top: 56px; }

  .contact {
    position: absolute;
    right: 30px;
    top: 92px;
    list-style: none;
    text-align: right;
  }
  .contact__item {
    color: var(--ink-white);
    font-size: 12px;
    line-height: 19px;
    display: flex;
    justify-content: flex-end;
    align-items: center;
    gap: 7px;
  }
  .contact__icon { width: 10px; height: 10px; fill: var(--brand-red); flex: none; }

  .takeover {
    position: absolute;
    right: 30px;
    top: 196px;
    color: var(--ink-white);
    font-size: 10px;
    font-weight: 700;
    letter-spacing: .35em;
    text-transform: uppercase;
  }

  .person { position: absolute; left: 48px; bottom: 30px; }
  .person__name { color: var(--ink-white); font-size: 22px; font-weight: 600; line-height: 1.1; }
  .person__role { color: var(--ink-dark); font-size: 12px; }
  .person__marks { position: absolute; left: -26px; top: 10px; display: flex; gap: 3px; }
  .person__marks span { width: 5px; height: 28px; background: var(--ink-white); }
  .person__marks span + span { background: var(--card-black); }

  .card--back .brand { right: 40px; top: 128px; }
  .card--back .brand__dot { width: 18px; height: 18px; }
  .card--back .brand__name { font-size: 24px; }
  .card--back .brand__tagline { right: 40px; top: 166px; font-size: 9px; }
</style>
</head>
<body>

<section class="card card--front" aria-label="Business card front">
  <svg class="card__band" viewBox="0 0 540 310" preserveAspectRatio="none" aria-hidden="true">
    <polygon points="0,128 430,310 0,310" fill="var(--brand-red)"/>
    <polygon points="0,120 450,310 430,310 0,128" fill="var(--ink-white)"/>
  </svg>

  <div class="brand"><span class="brand__dot"></span><span class="brand__name">Harwell Industrial Group</span></div>
  <p class="brand__tagline">Electrical · Mechanical · Airconditioning</p>

  <ul class="contact">
    <li class="contact__item">049-755-1832
      <svg class="contact__icon" viewBox="0 0 10 10"><path d="M2 0l2 2-1 1.5c.8 1.6 1.9 2.7 3.5 3.5L8 6l2 2-1.5 2C4 10 0 6 0 1.5z"/></svg></li>
    <li class="contact__item">tomwork@vandilo.com.au
      <svg class="contact__icon" viewBox="0 0 10 10"><path d="M0 2h10v6H0zM1 3v.4l4 2.6 4-2.6V3z"/></svg></li>
    <li class="contact__item">www.harwellindustrialgroup.com.au
      <svg class="contact__icon" viewBox="0 0 10 10"><circle cx="5" cy="5" r="4.5" fill="none" stroke="var(--brand-red)"/><path d="M0.5 5h9M5 .5v9" stroke="var(--brand-red)" stroke-width=".8"/></svg></li>
    <li class="contact__item">417 Calloway Street, Pembrook NSW 2458
      <svg class="contact__icon" viewBox="0 0 10 10"><path d="M5 0a3.5 3.5 0 0 1 3.5 3.5C8.5 6 5 10 5 10S1.5 6 1.5 3.5A3.5 3.5 0 0 1 5 0zm0 2a1.4 1.4 0 1 0 0 2.8A1.4 1.4 0 0 0 5 2z"/></svg></li>
  </ul>

  <p class="takeover">Barvo Group Pty Ltd</p>

  <div class="person">
    <div class="person__marks"><span></span><span></span></div>
    <h1 class="person__name">Tom Harwell</h1>
    <p class="person__role">Managing Director / Electrician</p>
  </div>
</section>

<section class="card card--back" aria-label="Business card back">
  <div class="brand"><span class="brand__dot"></span><span class="brand__name">Harwell Industrial Group</span></div>
  <p class="brand__tagline">Electrical · Mechanical · Airconditioning</p>
</section>

</body>
</html>
```